eBook cover and content: Steering Teams Beyond the Obvious Path

I teach a leadership program to companies that was developed at Vantrel and now need an eBook cover and content design. This downloadable eBook will be offered online in exchange for prospects' contact details. It needs to be designed with a sophisticated, senior HR executive audience in mind. There are some assets that are available for you to work with including photographs, a logo device for the program, and a colour palette (same as Vantrel's blue, green, yellow and red). Note that while the program was developed at Vantrel it is NOT a Vantrel product and I need to ensure that the eBook does not breach license guidelines. I have attached a very rough mockup of the content, images and graphic elements to help.

Target Market(s)

Senior business leaders and HR professionals.

Industry/Entity Type

Leadership

Font styles to use
Sans Serif

Requirements
Must have
• Keep it simple. Clean, contemporary, professional feel. This is a high-value decision for a company and needs to look modern, progressive and credible. Downloadable PDF. Easy to read and digest layout.
• Colours - see attached screenshot for red, blue, green, yellow ref. Additionally charcoal for most type and purple 330033 as extra colour is okay.
• Landscape format please.
Nice to have
• Plenty of white space.

```html
<!DOCTYPE html>
<html lang="en">
<head>
<meta charset="utf-8">
<title>Steering Teams Beyond the Obvious Path – eBook pages</title>
<link href="https://fonts.googleapis.com/css2?family=Raleway:wght@300;400;500;600;700&display=swap" rel="stylesheet">
<style>
  :root{
    --backdrop:#efefef;
    --paper:#ffffff;
    --accent-red:#e2372a;
    --accent-blue:#3d6db0;
    --accent-green:#34a853;
    --accent-yellow:#f4b400;
    --charcoal:#3a3a3a;
    --muted:#6d6d6d;
    --photo-light:#eceeef;
    --photo-mid:#c9cdd1;
  }
  *{margin:0;padding:0;box-sizing:border-box}
  html,body{width:1200px;height:851px;overflow:hidden;background:var(--backdrop)}
  body{position:relative;font-family:"Raleway",Arial,sans-serif;color:var(--charcoal)}

  .page{position:absolute;width:570px;height:396px;background:var(--paper);box-shadow:0 1px 3px rgba(0,0,0,.18)}
  .page--help{left:15px;top:20px}
  .page--featured{left:615px;top:20px}
  .page--reviews{left:15px;top:435px}
  .page--profile{left:615px;top:435px;overflow:hidden}

  .brand{position:absolute;left:22px;top:22px;display:flex;align-items:center;gap:5px;font-size:7px;font-weight:500;color:var(--charcoal)}
  .brand__dot{width:8px;height:8px;border-radius:50%;background:var(--accent-green)}

  .page-title{position:absolute;left:21px;top:60px;font-weight:400;font-size:19px;line-height:22px;color:var(--accent-red);letter-spacing:.3px;text-transform:uppercase}
  .page-title::after{content:"";display:block;width:58px;height:3px;background:var(--accent-red);margin-top:7px}

  .folio{position:absolute;right:0;bottom:10px;display:flex;align-items:center;gap:5px;font-size:7px;color:var(--accent-red)}
  .folio::after{content:"";width:7px;height:12px;background:var(--accent-red)}

  .body-copy{position:absolute;left:200px;top:63px;width:340px;font-size:8px;line-height:10.5px;color:var(--charcoal)}
  .body-copy p{margin-bottom:6px}
  .body-copy a{color:var(--accent-red);text-decoration:none}

  .press{position:absolute;left:200px;top:62px;width:340px}
  .press__item{margin-bottom:12px}
  .press__name{font-size:10px;font-weight:700;line-height:11px;color:var(--charcoal);margin-bottom:8px;display:flex;align-items:center;gap:4px}
  .press__mark{width:10px;height:10px;background:var(--accent-red)}
  .press__quote{font-size:7.6px;line-height:9.6px;color:var(--muted)}
  .press__more{font-size:6.5px;color:var(--accent-red);font-style:italic;margin-top:3px}

  .reviews{position:absolute;left:200px;top:62px;width:340px}
  .review{display:flex;gap:12px;margin-bottom:11px}
  .review__org{width:34px;flex:none;font-size:8px;font-weight:600;color:var(--charcoal);padding-top:14px;line-height:9px}
  .review__quote{font-size:8px;line-height:10.2px;color:var(--charcoal)}
  .review__by{font-size:6.2px;color:var(--accent-red);font-style:italic;margin-top:3px}

  .clients{position:absolute;left:205px;top:238px;width:300px;display:grid;grid-template-columns:repeat(3,1fr);row-gap:28px;justify-items:center}
  .client{font-size:10px;font-weight:600;color:var(--charcoal);display:flex;align-items:center;gap:4px}
  .client__dot{width:8px;height:8px;border-radius:50%;background:var(--charcoal)}

  .profile-photo{position:absolute;inset:0;background:linear-gradient(100deg,var(--photo-light) 0%,#f7f7f7 35%,var(--photo-mid) 75%,#aeb3b8 100%)}
  .profile-name{position:absolute;left:21px;top:60px;font-size:18px;font-weight:400;color:var(--accent-blue);letter-spacing:.3px}
  .profile-name::after{content:"";display:block;width:58px;height:2px;background:var(--accent-blue);margin-top:6px}
</style>
</head>
<body>

<section class="page page--help">
  <div class="brand"><span class="brand__dot"></span>Inner Compass Method</div>
  <h2 class="page-title">We'd love to<br>help you</h2>
  <div class="body-copy">
    <p>Boost performance. Enhance leadership. Elevate wellbeing.</p>
    <p>We believe in amplifying human potential with powerful, evidence-based principle and practices.</p>
    <p>We've had the privilege to teach ICM to some of Australia's hottest startups, as well as global tech giants and manufacturers.</p>
    <p>We've taught international retail and investment banks, multinational media companies and telcos.</p>
    <p>And we've taught at hospitals, holding companies, universities and professional services firms.</p>
    <p>We'd love to help you too.</p>
    <p>Tell us more about you, your organisation and your leadership development goals.</p>
    <p>Email <a href="mailto:icm@reedmarlowe.com">icm@reedmarlowe.com</a></p>
  </div>
  <div class="folio">10</div>
</section>

<section class="page page--featured">
  <div class="brand"><span class="brand__dot"></span>Inner Compass Method</div>
  <h2 class="page-title">Featured in</h2>
  <div class="press">
    <div class="press__item">
      <div class="press__name"><span class="press__mark"></span>Meridian Management Review</div>
      <p class="press__quote">'You know you could be a much more effective leader if you could approach each meeting with a fresh perspective. But in order to do that, you first need to put down the baggage you carried in from all your previous meetings. You can do it. And you can do it in just six seconds.'</p>
      <p class="press__more">&lt;&lt; read more</p>
    </div>
    <div class="press__item">
      <div class="press__name">Forward Works</div>
      <p class="press__quote">'Since the initial curriculum was developed specifically for Vantrel's engineers, it needed to be taught in a completely straightforward, secular language, explains Rourke, because scientists and engineers are typically skeptics. The course focuses on what's happening in the brain when you're having certain thoughts and feelings, and encourages reflection rather than reaction.'</p>
      <p class="press__more">&lt;&lt; read more</p>
    </div>
    <div class="press__item">
      <div class="press__name">Market Ledger</div>
      <p class="press__quote">'For me, the class was a much-needed opportunity to stop running, chewing, and cursing, and really notice what was happening — both around and inside me. Below, I've rounded up the insights from ICM that most resonated with me.'</p>
      <p class="press__more">&lt;&lt; read more</p>
    </div>
  </div>
  <div class="folio">13</div>
</section>

<section class="page page--reviews">
  <div class="brand"><span class="brand__dot"></span>Inner Compass Method</div>
  <h2 class="page-title">Recent<br>participants<br>and reviews</h2>
  <div class="reviews">
    <div class="review">
      <div class="review__org">Vantrel</div>
      <div>
        <p class="review__quote">"ICM has had a tremendous impact on me and my team. We're clear, calmer and sharper for it and we're playing together nicely. Many of the practices are woven into our daily lives."</p>
        <p class="review__by">Nora Vell, Creative Director, Vantrel Studio Lab</p>
      </div>
    </div>
    <div class="review">
      <div class="review__org">Harbour Coast</div>
      <div>
        <p class="review__quote">"The concepts are simple, accessible and translatable and made a huge impression on our emergency department team. I wholeheartedly recommend this program."</p>
        <p class="review__by">Dr Amira Solano, Harbour Coast Hospital, Emergency Department</p>
      </div>
    </div>
    <div class="review">
      <div class="review__org">ORBIT</div>
      <div>
        <p class="review__quote">"ICM has been the training highlight of the year at ORBIT. All participants have reported significant improvement in their professional and personal lives."</p>
        <p class="review__by">Leon Fairweather, People and Development Director, ORBIT</p>
      </div>
    </div>
  </div>
  <div class="clients">
    <span class="client"><span class="client__dot"></span>Calder</span>
    <span class="client">Norvane</span>
    <span class="client">Pellio</span>
    <span class="client">Tessar</span>
    <span class="client">Aurik</span>
    <span class="client">Quillo</span>
    <span class="client">Brindle</span>
    <span class="client">Solvex</span>
    <span class="client">Eastgate</span>
  </div>
  <div class="folio">11</div>
</section>

<section class="page page--profile">
  <div class="profile-photo" role="img" aria-label="Portrait photograph of the program facilitator seated in a white shirt in a bright, softly lit room"></div>
  <h2 class="profile-name">REED MARLOWE</h2>
</section>

</body>
</html>
```